New Business Card Design Project

The idea, the card is to put a card, which contains two companies at the same time. Please see the attached data and idea of how the current cards are.
VELMIR
Constructora
Ferrepiezas Caliza SRL.
Equipos para Plantas de Tratamientos y Acueductos, Alquiler de Equipos Pesados para la Construcción.
C / Tomás Urbina No.47
Barrio Lucero, Santo Domingo. República Dominicana.
Tel .: 1809 512 4476
CEL: 1829 746 2158
oriol@ferrepiezascaliza.example
velmirconstrution@correo-ejemplo.example
www.ferrepiezascaliza.example
Velmir construction.
Es una empresa constructora.
NOTA: La idea es llevar una sola tarjeta para dos compañías. o si no resulta hacer un diseño en cada lado, uno para cada empresa.Equipos para Plantas de Tratamiento y Acueductos, Alquiler de Equipos Pesados para la Construcción.
Deben de llevar, los logos.
VELMIR
Constructora
Ferrepiezas Caliza SRL.
C / Tomás Urbina No.47
Tel .: 1809 512 4476
CEL: 1829 746 2158
Velmir construction.
VELMIR
Constructora
Ferrepiezas Caliza SRL.
C / Tomás Urbina No.47
Tel .: 1809 512 4476
CEL: 1829 746 2158
Velmir construction.
It is a construction company
NOTE: The idea is to carry a single card for two companies. or if it does not turn out to make a design on each side, one for each company. Equipment for Treatment Plants and Aqueducts, Rental of Heavy Equipment for Construction.
They must carry, the logos.
How is the design similar to that, send example, for data, from previous designs.
What I'm looking for is a new design, not a remodeled copy
ferrepiezascaliza
Tel: 1809 542 4476
cel: 1829 746 2158
oriol@gerrepiezascaliza.example
Direccion:
C/ Tomás Urbina # 47
Barrio lucero, Santo Domingo
Republica Dominicana
Velmir
constructora
Tel: 1809 358-1047
Cel: 1829 746 2158
velmirsa1@correo-ejemplo.example
Direccion:
C/ Tomás Urbina # 47
Republica Dominicana
FERREPIEZAS CALIZA, S.R.L.
C/ Ramiro Olmedo Lasta esquina Tomás Urbina # 47
Barrio Lucero, Santo Domingo, República Dominicana
Office: 809.542.4476
Fax: 809.594.7361
Cel (Local): 829 746 2158
E-mail: MUESTRA@MUESTRA.example
E-mail:MUESTRA@correo-ejemplo.example
Website: http://www.MUESTRA.example

```html
<!DOCTYPE html>
<html lang="es">
<head>
<meta charset="utf-8">
<title>Tarjeta de presentación – Ferrepiezas Caliza / Velmir</title>
<link rel="stylesheet" href="https://fonts.googleapis.com/css2?family=Montserrat:wght@400;500;700;800&display=swap">
<style>
  :root {
    --page-bg: #e9f0cc;
    --card-bg: #ffffff;
    --ink: #2f2f2f;
    --accent: #e8601c;
    --soft-peach: #fbe6d6;
    --soft-cream: #fdf3e0;
    --card-edge: #3a3a3a;
  }
  * { box-sizing: border-box; margin: 0; padding: 0; }
  html, body {
    width: 802px; height: 1200px; overflow: hidden;
    background: var(--page-bg);
    font-family: "Montserrat", sans-serif;
  }
  .canvas {
    position: relative; width: 802px; height: 1200px;
  }
  .business-card {
    position: absolute; left: 50px; top: 400px;
    width: 702px; height: 401px;
    background: var(--card-bg);
    border: 1px solid var(--card-edge);
    border-bottom: none;
    overflow: hidden;
  }
  .backdrop-area {
    position: absolute; right: 20px; top: 128px;
    width: 270px; height: 255px;
    background: linear-gradient(160deg, var(--soft-cream), var(--soft-peach) 70%, rgba(251,230,214,0.3));
    opacity: 0.55;
  }
  .company-name {
    position: absolute; left: 39px; top: 44px;
    font-size: 16.5px; font-weight: 500; letter-spacing: 1.2px;
    color: var(--accent);
  }
  .brand {
    position: absolute; right: 23px; top: 52px;
    display: flex; align-items: center; gap: 12px;
  }
  .brand-square {
    width: 38px; height: 38px; background: var(--accent);
  }
  .brand-name {
    font-size: 50px; font-weight: 800; line-height: 1;
    color: var(--ink); letter-spacing: -1px;
  }
  .contact-list {
    position: absolute; left: 38px; top: 200px;
    list-style: none;
  }
  .contact-item {
    display: flex; align-items: flex-start; gap: 17px;
    margin-bottom: 9px;
    font-size: 13px; letter-spacing: 0.9px; line-height: 15.5px;
    color: var(--ink);
  }
  .contact-icon { width: 17px; height: 17px; flex: none; margin-top: -1px; }
  .contact-icon svg { display: block; }
  .accent-bar {
    position: absolute; left: 0; bottom: 0;
    width: 100%; height: 6px; background: var(--accent);
  }
</style>
</head>
<body>
<main class="canvas">
  <section class="business-card">
    <div class="backdrop-area" role="img" aria-label="Fondo decorativo suave en tonos crema y melocotón"></div>

    <p class="company-name">FERREPIEZAS CALIZA, S.R.L.</p>

    <div class="brand">
      <span class="brand-square"></span>
      <span class="brand-name">VELMIR</span>
    </div>

    <ul class="contact-list">
      <li class="contact-item">
        <span class="contact-icon">
          <svg width="17" height="17" viewBox="0 0 17 17" fill="none" stroke="var(--accent)" stroke-width="1.2">
            <circle cx="8.5" cy="8.5" r="7.6"/>
            <path d="M8.5 12.5 C6.5 10 5.8 8.6 5.8 7.4 a2.7 2.7 0 0 1 5.4 0 c0 1.2-.7 2.6-2.7 5.1z"/>
            <circle cx="8.5" cy="7.4" r="0.9"/>
          </svg>
        </span>
        <span>C/ Ramiro Olmedo Lasta esquina Tomás Urbina # 47<br>Barrio Lucero, Santo Domingo,<br>República Dominicana</span>
      </li>
      <li class="contact-item">
        <span class="contact-icon">
          <svg width="17" height="17" viewBox="0 0 17 17" fill="none" stroke="var(--accent)" stroke-width="1.2">
            <circle cx="8.5" cy="8.5" r="7.6"/>
            <path d="M5.6 5 l1.5-.4 1 2-1 .8 c.4 1 1.1 1.7 2.1 2.1 l.8-1 2 1-.4 1.5 c-3.1.3-6.3-2.9-6-6z"/>
          </svg>
        </span>
        <span>Office: 809.542.4476<br>Fax: 809.594.7361<br>Cel (Local): 829 746 2158</span>
      </li>
      <li class="contact-item">
        <span class="contact-icon">
          <svg width="17" height="17" viewBox="0 0 17 17" fill="none" stroke="var(--accent)" stroke-width="1.2">
            <circle cx="8.5" cy="8.5" r="7.6"/>
            <rect x="5" y="6" width="7" height="5"/>
            <path d="M5 6 l3.5 2.8 L12 6"/>
          </svg>
        </span>
        <span>E-mail: MUESTRA@MUESTRA.example<br>E-mail:MUESTRA@correo-ejemplo.example</span>
      </li>
      <li class="contact-item">
        <span class="contact-icon">
          <svg width="17" height="17" viewBox="0 0 17 17" fill="none" stroke="var(--accent)" stroke-width="1.2">
            <circle cx="8.5" cy="8.5" r="7.6"/>
            <path d="M1 8.5 h15 M8.5 1 c-3 3-3 12 0 15 M8.5 1 c3 3 3 12 0 15"/>
          </svg>
        </span>
        <span>www.MUESTRA.example</span>
      </li>
    </ul>

    <div class="accent-bar"></div>
  </section>
</main>
</body>
</html>
```